Affinity Card (Brochure for a Fuel Card )

We need a brochure developed for a Fuel Card our company is offering to the market. Our offer has many different elements to it and as well as the benefits of the card it has geographical spread across Australia where the card is taken and where we can offer lucrative deals . The design should show the benefits of our card and also the fact it has the ability to be used Nationally as well as locally. The final design should communicate that the card is linked to both Halcyon and Corvane (cant use the corvane logo)
The design should have a section for the applicant to put his name and address , l have supplied an example from America but want it different
It can have up to 4 folds no issues
Below are ideas for use

Target Market(s)

Fuel Card Users in all segments

Industry/Entity Type

It Company

Requirements
Must have
• Be able to capture attention and be handed out
• We now need the use of the Corvane sites in the brochure and drop the truck top image
• Sorry about the changes

```html
<!DOCTYPE html>
<html lang="en">
<head>
<meta charset="utf-8">
<title>Halcyon Corvane Fuel Card Brochure – Inside Spread</title>
<link href="https://fonts.googleapis.com/css2?family=Arimo:wght@700&family=Open+Sans:ital,wght@0,400;1,400&display=swap" rel="stylesheet">
<style>
  :root{
    --ink:#111111;
    --muted:#333333;
    --panel-blue:#4a8fd0;
    --accent-blue:#4e8fd3;
    --accent-red:#e8262f;
    --white:#ffffff;
    --rule:#b58aa0;
    --map-land:#e8e4da;
    --map-water:#a9c7e8;
    --photo-dark:#2f3a44;
    --photo-mid:#9aa7b1;
  }
  *{box-sizing:border-box;margin:0;padding:0}
  html,body{width:1200px;height:743px;overflow:hidden;background:var(--white)}
  .spread{position:relative;width:1200px;height:743px;overflow:hidden;font-family:"Open Sans",Arial,sans-serif;color:var(--ink)}
  .panel{position:absolute;top:0;height:743px}
  .panel--left{left:0;width:407px;background:var(--white)}
  .panel--middle{left:407px;width:386px;background:var(--panel-blue);color:var(--white)}
  .panel--right{left:793px;width:407px;background:var(--white)}

  .heading{font-family:"Arimo",Arial,sans-serif;font-weight:700;font-size:12.5px;letter-spacing:.1px;text-transform:uppercase}
  .list{list-style:none;font-style:italic;font-size:11.5px;line-height:19.2px;color:var(--ink)}

  .account{position:absolute;left:21px;top:40px;width:380px}
  .account .heading{margin-bottom:6px}
  .divider-left{position:absolute;left:21px;top:277px;width:365px;border-top:1px dotted var(--rule)}
  .cards{position:absolute;left:21px;top:291px;width:380px}
  .cards .heading{margin-bottom:6px}

  .map-area{position:absolute;left:0;top:395px;width:407px;height:348px}

  .security{position:absolute;left:22px;top:40px;width:345px}
  .security .heading{color:var(--white);margin-bottom:8px}
  .lead{font-size:12px;line-height:17px;margin-bottom:10px}
  .bullets{list-style:none;font-style:italic;font-size:10.3px;line-height:14.5px;margin-left:0}
  .bullets li{position:relative;padding-left:19px;margin-bottom:13px;text-align:justify}
  .bullets li::before{content:"";position:absolute;left:0;top:5px;width:5px;height:5px;background:var(--white)}
  .lead--second{margin-top:12px;margin-bottom:8px}
  .divider-middle{position:absolute;left:22px;top:419px;width:343px;border-top:1px dotted rgba(255,255,255,.75)}
  .locations{position:absolute;left:22px;top:435px;width:345px}
  .locations .heading{color:var(--white);line-height:15px;margin-bottom:11px}
  .locations .bullets li{margin-bottom:7.5px}

  .photo-area{position:absolute;left:0;top:0;width:407px;height:445px}
  .feature{position:absolute;left:19px;width:368px}
  .feature .heading{margin-bottom:2px;font-size:12px}
  .feature p{font-size:9.6px;line-height:14.5px;text-align:justify;margin-bottom:10px;color:var(--ink)}
  .feature--one{top:405px}
  .feature--two{top:579px}
</style>
</head>
<body>
<main class="spread">

  <section class="panel panel--left">
    <div class="account">
      <h2 class="heading">Reduce fraud risk - manage your account online</h2>
      <ul class="list">
        <li>(i) Download Statements</li>
        <li>(ii) Concise fleet reporting</li>
        <li>(iii) Automatic reporting</li>
        <li>(iv) Odometer audits</li>
        <li>(v) Transaction extracts</li>
        <li>(vI) Cost centre summary</li>
        <li>(vii) Litres per 100km</li>
        <li>(viii) Active card listings</li>
        <li>(ix) Expiring fuel cards</li>
        <li>(x) Exception reports</li>
      </ul>
    </div>
    <div class="divider-left"></div>
    <div class="cards">
      <h2 class="heading">Customised card management</h2>
      <ul class="list">
        <li>(i) Card management – order, delete, suspend and alter cards. Manage cost centres &amp; set pins</li>
        <li>(ii) Shop sales option</li>
        <li>(iii) Truck wash option</li>
      </ul>
    </div>

    <svg class="map-area" viewBox="0 0 407 348" width="407" height="348">
      <defs>
        <linearGradient id="mapTone" x1="0" y1="0" x2="0.4" y2="1">
          <stop offset="0" stop-color="var(--map-land)"/>
          <stop offset="0.7" stop-color="#dfe3d6"/>
          <stop offset="1" stop-color="var(--map-water)"/>
        </linearGradient>
      </defs>
      <polygon points="0,3 407,120 407,348 0,348" fill="url(#mapTone)" role="img" aria-label="Map of Victorian region marking card acceptance sites around Melbourne"/>
      <polygon points="0,0 407,105 407,118 0,6" fill="var(--accent-red)"/>
      <polygon points="0,6 407,118 407,150 150,60" fill="var(--accent-blue)"/>
    </svg>
  </section>

  <section class="panel panel--middle">
    <div class="security">
      <h2 class="heading">Security</h2>
      <p class="lead">We recognise that card security is a priority for all customers</p>
      <ul class="bullets">
        <li>Personal Identification Number (PIN) - the preferred security measure, PINs can be used for vehicle specific cards and for those cardholders who prefer a PIN instead of a signature</li>
        <li>Signature - used in cases where the card will only be used by an individual cardholder.</li>
        <li>Odometer readings - when selected, cardholders will be prompted to supply odometer readings to the console operator at time of purchase. The use of odometer readings provides additional tracking measures for the organisation.</li>
        <li>Purchase limits - can also be nominated on individual cards and will restrict purchases by time, volume or dollars</li>
      </ul>
      <p class="lead lead--second">Control /Flexibility/ Simplicity and Convenience the cornerstone of our card offer</p>
      <ul class="bullets">
        <li>We let and enable you to control your cards and your business in the simplest possible way</li>
        <li>Payment terms up to 50 days from transaction</li>
      </ul>
    </div>
    <div class="divider-middle"></div>
    <div class="locations">
      <h2 class="heading">24 hour truck locations<br>we have developed for you</h2>
      <ul class="bullets">
        <li>Laverton – 1-13 Ferris Road Laverton North Victoria.</li>
        <li>Merredin – Lot 1402 Brindle Crescent Merredin WA 6415</li>
        <li>Roma – 58 Harlow Street Roma Qld 4455</li>
        <li>Griffith – 4-8 Tamsin Avenue Griffith NSW 2680</li>
        <li>Warwick – 9 Ashcombe Street Warwick QLD 4370</li>
        <li>Bendigo – 121 Pellam Road Bendigo Victoria 3550</li>
        <li>Benalla – Ridgeway Highway Benalla Victoria.</li>
        <li>Katanning – 14 Corran Street Katanning WA 6317</li>
        <li>Katherine – Cnr Talbot Drive and Marlow Crescent Katherine NT 0850</li>
      </ul>
    </div>
  </section>

  <section class="panel panel--right">
    <svg class="photo-area" viewBox="0 0 407 445" width="407" height="445">
      <defs>
        <linearGradient id="photoTone" x1="0" y1="0" x2="1" y2="1">
          <stop offset="0" stop-color="var(--photo-mid)"/>
          <stop offset="0.55" stop-color="#c9a48d"/>
          <stop offset="1" stop-color="var(--photo-dark)"/>
        </linearGradient>
      </defs>
      <polygon points="0,0 407,0 407,395 0,330" fill="url(#photoTone)" role="img" aria-label="Photograph of two business people shaking hands"/>
      <polygon points="90,0 407,0 407,100" fill="var(--white)"/>
      <polygon points="90,0 140,0 407,80 407,100" fill="var(--accent-red)"/>
      <polygon points="140,0 230,0 407,52 407,80" fill="var(--accent-blue)"/>
      <polygon points="0,330 407,395 407,445" fill="var(--white)"/>
      <polygon points="0,318 407,388 407,398 0,334" fill="var(--accent-red)"/>
      <polygon points="0,334 407,398 407,430" fill="#1c1c1c"/>
    </svg>

    <article class="feature feature--one">
      <h3 class="heading">Lorem ipsum dolor</h3>
      <p>Lorem Ipsum is simply dummy text of the printing and typesetting industry. Lorem Ipsum has been the industry's standard dummy text ever since the 1500s, when an unknown printer took a galley of type and scrambled it to make a type specimen book. It has survived not only five centuries, but also the leap into electronic typesetting, remaining essentially unchanged.</p>
      <p>Lorem Ipsum is simply dummy text of the printing and typesetting industry. Lorem Ipsum has been the industry's standard dummy text ever since the 1500s, when an unknown printer took a galley of type and scrambled it to make a type specimen book. It has survived not only five centuries, but also the leap into electronic typesetting, remaining essentially unchanged.</p>
    </article>
    <article class="feature feature--two">
      <h3 class="heading">Lorem ipsum dolor</h3>
      <p>Lorem Ipsum is simply dummy text of the printing and typesetting industry. Lorem Ipsum has been the industry's standard dummy text ever since the 1500s, when an unknown printer took a galley of type and scrambled it to make a type specimen book. It has survived not only five centuries, but also the leap into electronic typesetting, remaining essentially unchanged.</p>
      <p>Lorem Ipsum is simply dummy text of the printing and typesetting industry. Lorem Ipsum has been the industry's standard dummy text ever since the 1500s, when an unknown printer took a galley of type and scrambled it to make a type specimen book was there.</p>
    </article>
  </section>

</main>
</body>
</html>
```